90 Day Landing Page for Online Coaching

Need a website design that’s gonna be used for an online coaching landing page (details in the WORD document). The colors/design can be complimentary to the program called, The Quarter-Year Tycoon; the banners are attached in the document
There are alot of extra photos that you can use but none of them are required; use as needed.
We don’t have the URL yet, but we intend to use a single landing page.

Target Market(s)

for men and women looking to launch a business

Industry/Entity Type

business consulting

Requirements
Must have
• the copy attached

```html
<!DOCTYPE html>
<html lang="en">
<head>
<meta charset="utf-8">
<title>The Quarter-Year Tycoon — Landing Page</title>
<link rel="stylesheet" href="https://fonts.googleapis.com/css2?family=Inter:wght@400;500;600;700;800&family=Source+Serif+4:wght@400;500;600&family=Oswald:wght@400;500&display=swap">
<style>
:root{
  --blue-deep:#0b4c9c;
  --blue-mid:#1460b4;
  --accent:#3a7fe0;
  --line:#7fb0f0;
  --cyan:#d3f6fb;
  --paper:#f3f5f8;
  --sky:#e2edfb;
  --ink:#1d1f24;
  --muted:#5d6470;
  --green:#22b35e;
  --orange:#f5a321;
  --white:#ffffff;
}
*{box-sizing:border-box;margin:0;padding:0}
html,body{width:1200px;height:1200px;overflow:hidden;background:var(--white)}
.stage{position:absolute;left:0;top:0;width:1932px;height:1932px;transform:scale(0.621118);transform-origin:0 0}
.page{position:absolute;left:714px;top:0;width:504px;height:1932px;overflow:hidden;font-family:"Inter",sans-serif;color:var(--ink)}
.abs{position:absolute}
.serif{font-family:"Source Serif 4",serif}
.hl{color:var(--accent)}
.photo{position:absolute;border-radius:4px;background:linear-gradient(150deg,#c9b7a4,#5d4a3e 60%,#2a2522)}
.tag{position:absolute;background:#111;color:#fff;font-size:3.2px;font-weight:600;padding:1px 3px;border-radius:2px;letter-spacing:.2px}

.band-hero{left:0;top:0;width:504px;height:283px;background:linear-gradient(120deg,#c9f4fa 0%,#f6fdff 35%,#ffffff 60%)}
.band-hero-blue{left:283px;top:0;width:221px;height:283px;background:var(--blue-deep)}
.band-motivation{left:0;top:283px;width:504px;height:283px;background:radial-gradient(circle at 0% 20%,#c8f3f8 0,rgba(200,243,248,0) 45%),var(--paper)}
.band-mission{left:0;top:566px;width:504px;height:337px;background:radial-gradient(circle at 92% 8%,#c9f4fa 0,rgba(201,244,250,0) 30%),radial-gradient(circle at 10% 100%,#c9f4fa 0,rgba(201,244,250,0) 45%),#f6f9fb}
.band-cta{left:0;top:903px;width:504px;height:146px;background:linear-gradient(180deg,#0f62b0,var(--blue-deep))}
.band-tips{left:0;top:1049px;width:504px;height:254px;background:linear-gradient(180deg,#e8f1fc,var(--sky))}
.band-coaches{left:0;top:1303px;width:504px;height:613px;background:var(--blue-deep)}
.band-foot{left:0;top:1916px;width:504px;height:16px;background:#eef1f5}

.brand{left:43px;top:8px;font-weight:800;font-size:4.6px;line-height:5px;color:#111;letter-spacing:.1px;width:60px}
.nav{left:118px;top:8px;width:344px;height:14px;background:#fff;border-radius:3px;box-shadow:0 0 0 .6px #d6dde6;display:flex;align-items:center;justify-content:space-between;padding:0 5px;font-size:4.2px;color:#333}
.nav .on{background:#111;color:#fff;padding:1.5px 3px;border-radius:2px}

.hero-title{left:42px;top:58px;font-size:19.5px;line-height:25px;font-weight:400;color:#1b1b1b}
.hero-title .box{color:var(--accent);box-shadow:0 0 0 .6px #b9d3f5;padding:0 1px}
.hero-sub{left:42px;top:138px;width:232px;font-size:5px;line-height:10px;color:#555}
.gallery-label{left:42px;top:179px;font-size:7.5px}
.thumb-count{display:flex;align-items:center;justify-content:center;color:#fff;font-size:10px;font-weight:500}
.play{position:absolute;left:42px;top:28px;width:18px;height:18px;border-radius:50%;border:1px solid rgba(255,255,255,.8);background:rgba(255,255,255,.25)}

.promo{left:305px;top:61px;width:157px;height:157px;border-radius:8px;border:1.5px solid #dfe9f7;background:linear-gradient(180deg,#1a6cc4,#0a3f86);overflow:hidden}
.promo-name{position:absolute;left:0;top:4px;width:100%;text-align:center;color:#fff;font-weight:800;font-size:7.5px;line-height:9px}
.promo-photo{left:18px;top:26px;width:120px;height:78px;background:linear-gradient(180deg,#2767b5,#0e2f5f)}
.promo-line{position:absolute;left:0;top:110px;width:100%;text-align:center;color:#fff;font-weight:800;font-size:8.6px;line-height:11px}
.promo-cta{position:absolute;left:0;top:142px;width:100%;text-align:center;color:#fff;font-weight:700;font-size:4.6px}
.stats{left:305px;top:236px;width:157px;display:flex;justify-content:space-between;color:#cfe0f6}
.stat i{display:block;width:7px;height:7px;border:.7px solid #8fb6e8;border-radius:2px;margin-bottom:4px}
.stat b{display:block;font-weight:500;font-size:7px;color:#fff}
.stat span{display:block;font-size:3.6px;margin-top:1px}

.mot-title{left:59px;top:353px;font-size:8.5px}
.hub{left:123px;top:423px;width:48px;height:48px;border-radius:50%;border:1.5px solid #9cc0ee;background:#fff}
.hub .photo{left:4px;top:4px;width:37px;height:37px;border-radius:50%;background:linear-gradient(160deg,#7a8da8,#1f2d44)}
.bubble{position:absolute;background:#fff;border:.6px solid #d7dde6;border-radius:3px;font-size:3.5px;line-height:5.2px;color:#444;text-align:center;padding:3px 3px;display:flex;align-items:center;justify-content:center}
.note{left:316px;top:408px;width:146px;height:130px;background:#fff;border-radius:5px;box-shadow:0 2px 8px rgba(20,40,80,.12);padding:10px 10px}
.note h3{font-family:"Source Serif 4",serif;font-weight:400;font-size:7.6px;line-height:12px;margin-bottom:7px}
.note p{font-size:3.6px;line-height:5.4px;color:#444;margin-bottom:5px}

.center-head{left:0;width:504px;text-align:center}
.mis-title{top:589px;font-size:8.5px}
.frame{left:199px;top:611px;width:103px;height:95px;border:1.2px solid var(--accent);border-radius:5px;background:#fff}
.frame .photo{left:6px;top:6px;width:89px;height:81px;background:linear-gradient(160deg,#b89a7e,#3b2d2c 55%,#1d2d55)}
.gain{position:absolute;width:66px;height:35px;background:#fff;border:.6px solid #d4dce7;border-radius:3px;font-size:3.6px;line-height:4.6px;color:#333;padding:3px 3px 3px 13px;display:flex;align-items:center}
.gain::before{content:"";position:absolute;left:4px;top:50%;margin-top:-2.5px;width:5px;height:5px;border-radius:50%;background:var(--green)}
.gain::after{content:"";position:absolute;left:5.4px;top:50%;margin-top:-1.6px;width:1.6px;height:2.6px;border:solid #fff;border-width:0 .6px .6px 0;transform:rotate(45deg)}

.quote{left:42px;top:735px;width:419px;height:125px;border:1.4px solid var(--accent);border-radius:6px;background:#fff}
.quote.dark{top:1751px;height:138px;background:var(--blue-deep);border-color:#4f8fe2}
.q-photo{position:absolute;left:55px;top:12px;width:88px;height:88px;border-radius:50%;background:radial-gradient(circle at 50% 40%,#9a6e55,#4a2e24 60%,#c92730 100%)}
.quote.dark .q-photo{left:54px;top:18px;background:radial-gradient(circle at 50% 40%,#8a6048,#3a261e 60%,#1e2f52 100%)}
.arrow{position:absolute;top:57px;width:11px;height:11px;border:.6px solid #b9c3d0;border-radius:2px;font-size:7px;line-height:10px;text-align:center;color:#778}
.quote.dark .arrow{top:63px;border-color:#6c98d6;color:#cfe0f6}
.dots{position:absolute;left:89px;top:110px;display:flex;gap:2px}
.dots i{width:2px;height:2px;border-radius:50%;background:#c6ccd6}
.dots i:first-child{background:#222}
.quote.dark .dots{top:116px}
.quote.dark .dots i{background:#6f93c4}
.quote.dark .dots i:first-child{background:#fff}
.q-body{position:absolute;left:166px;top:12px;width:200px}
.q-body h3{font-family:"Source Serif 4",serif;font-weight:400;font-size:7.5px;margin:8px 0 7px}
.q-body p{font-size:3.6px;line-height:5.4px;color:#555;margin-bottom:5px}
.q-body .by{font-size:3.2px;font-weight:600;color:#333;margin-top:10px}
.quote.dark .q-body{left:186px;top:14px;width:186px}
.quote.dark h3{font-family:"Oswald",sans-serif;font-size:8px;color:#fff}
.quote.dark h3 .hl{color:#9cc5ff}
.quote.dark p{color:#d5e3f7}
.quote.dark .by{color:#fff}

.cta-card{left:49px;top:935px;width:394px;height:84px;background:linear-gradient(90deg,#fff 55%,#dbe9fb);border-radius:5px;box-shadow:0 3px 10px rgba(0,0,0,.2)}
.cta-text{left:74px;top:949px;width:245px;text-align:center;font-size:8px;line-height:12.5px}
.cta-text .go{color:var(--green)}
.cta-banner{left:72px;top:984px;width:174px;height:20px;border-radius:2px;background:linear-gradient(90deg,#0f5cb2,#0a3d85);display:flex;align-items:center;justify-content:space-between;padding:0 5px;color:#fff;font-weight:800;font-size:4.4px;line-height:5px}
.cta-banner .mid{width:40px;height:17px;background:linear-gradient(180deg,#2f70bf,#153e78)}
.btn{left:262px;top:984px;width:52px;height:19px;border-radius:3px;background:var(--orange);color:#fff;font-size:5px;font-weight:600;display:flex;align-items:center;justify-content:center}
.cta-person{left:330px;top:899px;width:92px;height:120px;border-radius:40px 40px 0 0;background:linear-gradient(180deg,#6d4a38 0,#1e1b1d 40%,#161416)}

.tips-title{left:75px;top:1081px;font-size:8px;line-height:11px}
.tips-note{left:229px;top:1073px;width:232px;height:88px;border:1.2px solid #8fb6ea;border-radius:6px}
.tips-note p{position:absolute;left:26px;top:14px;width:180px;font-size:4.2px;line-height:7px;color:#555}
.killer{position:absolute;top:1117px;width:112px;height:145px;border-radius:4px;overflow:hidden;background:#fff}
.killer .photo{left:0;top:0;width:112px;height:72px;border-radius:0}
.killer .txt{position:absolute;left:0;top:66px;width:112px;height:79px;background:#fff;border-radius:4px 4px 0 0;padding:5px 6px}
.killer b{display:inline-block;background:#e7ebf1;font-size:3px;font-weight:500;padding:1px 3px;border-radius:2px;margin-bottom:3px}
.killer h4{font-family:"Source Serif 4",serif;font-weight:400;font-size:5.6px;margin-bottom:4px}
.killer p{font-size:3.6px;line-height:5.2px;color:#444}

.coach-head{top:1323px;color:#fff;font-size:8px}
.coach-head .hl{color:#9cc5ff}
.tabs{left:157px;top:1348px;width:190px;height:19px;border:.8px solid #fff;border-radius:3px;display:flex;align-items:center;padding:2px;color:#fff;font-size:6.5px;white-space:nowrap}
.tabs .on{background:#1c2230;padding:2px 6px;border-radius:2px;margin-right:9px}
.fact{position:absolute;width:120px;height:49px;background:#fff;border-radius:3px;padding:8px 6px 6px 30px;font-size:3.3px;line-height:4.9px;color:#444}
.fact b{color:#111}
.fact i{position:absolute;left:10px;top:17px;width:10px;height:12px;border:.7px solid #55709a;border-radius:2px}
.logos{left:63px;top:1492px;width:377px;height:32px;background:#fff;border-radius:3px;display:flex;align-items:center;justify-content:space-around;padding:0 6px}
.logos i{display:block;width:30px;height:9px;border-radius:2px;background:#c9cfd8}
.pic{position:absolute;border-radius:4px}
</style>
</head>
<body>
<div class="stage">
<main class="page">

  <div class="abs band-hero"></div>
  <div class="abs band-hero-blue"></div>
  <div class="abs band-motivation"></div>
  <div class="abs band-mission"></div>
  <div class="abs band-cta"></div>
  <div class="abs band-tips"></div>
  <div class="abs band-coaches"></div>
  <div class="abs band-foot"></div>

  <svg class="abs" style="left:0;top:0" width="504" height="1932" viewBox="0 0 504 1932" fill="none">
    <g stroke="#7fb0f0" stroke-width="1.2">
      <path d="M283 0 V305 Q283 316 272 316 H53 Q42 316 42 327 V541 Q42 552 53 552 H240 Q251 552 251 563 V611"/>
      <path d="M251 706 V735 M251 860 V903"/>
      <rect x="292" y="332" width="100" height="78" rx="6"/>
      <path d="M42 1063 V1279 Q42 1290 53 1290 H240 Q251 1290 251 1301 V1303"/>
      <path d="M251 1716 V1751 M251 1889 V1932" stroke="#5d93dc"/>
      <path d="M251 1303 V1316" stroke="#5d93dc"/>
    </g>
    <g stroke="#c4cdd8" stroke-width=".6">
      <path d="M147 447 L106 417 M147 447 L189 417 M147 447 L110 448 M147 447 L187 450 M147 447 L115 490 M147 447 L183 492 M147 447 L148 504"/>
    </g>
  </svg>

  <div class="abs brand">THE QUARTER-YEAR<br>TYCOON</div>
  <nav class="abs nav">
    <span class="on">Home</span><span>Motivation</span><span>Our Mission</span><span>Real Win</span><span>Tips</span><span>Meet Coaches</span><span>Be Inspired</span><span>What You Get</span><span>Real Results</span><span>FAQ</span>
  </nav>

  <h1 class="abs hero-title serif">It’s Your <span class="box">Turn!</span><br>The Launch a Million<br>Dollar Brand in 90 Days!</h1>
  <p class="abs hero-sub">is a 90-Days Sprint that helps you turn your idea, skill, or passion into a brand that makes money - fast</p>
  <p class="abs gallery-label serif">Our <span class="hl">Gallery</span></p>
  <div class="photo" style="left:42px;top:196px;width:104px;height:72px" role="img" aria-label="Coach speaking on stage to an audience"><span class="play"></span></div>
  <div class="photo" style="left:155px;top:211px;width:47px;height:42px;background:linear-gradient(160deg,#b8a693,#2a2f44)" role="img" aria-label="Both coaches posing together"></div>
  <div class="photo thumb-count" style="left:211px;top:211px;width:47px;height:42px;background:linear-gradient(160deg,#8a5b5b,#3a2428)" role="img" aria-label="More gallery photos">10+</div>

  <div class="abs promo">
    <div class="promo-name">THE QUARTER-YEAR<br>TYCOON</div>
    <div class="photo promo-photo" role="img" aria-label="The two coaches standing side by side"></div>
    <div class="promo-line">LAUNCH A MILLION DOLLAR<br>BRAND IN 90 DAYS</div>
    <div class="promo-cta">SIGN UP TODAY!</div>
  </div>
  <div class="abs stats">
    <div class="stat"><i></i><b>10 Years</b><span>Experience</span></div>
    <div class="stat"><i></i><b>99.8%</b><span>Satisfaction</span></div>
    <div class="stat"><i></i><b>256+</b><span>Clients</span></div>
  </div>

  <span class="tag" style="left:59px;top:344px">MOTIVATION</span>
  <h2 class="abs mot-title serif">Does This Sound <span class="hl">Like You</span>?</h2>
  <div class="abs hub"><div class="photo" role="img" aria-label="Coach portrait"></div></div>
  <div class="bubble" style="left:80px;top:385px;width:51px;height:32px">You want to escape the paycheck to paycheck grind and build real wealth</div>
  <div class="bubble" style="left:164px;top:385px;width:50px;height:32px">You have good ideas but can't figure out how to turn them into steady income</div>
  <div class="bubble" style="left:58px;top:431px;width:52px;height:34px">You want a life where your schedule, income, and future are up to you, not someone else</div>
  <div class="bubble" style="left:187px;top:433px;width:50px;height:34px">You've tried launching a business, but it didn't work out the way you hoped</div>
  <div class="bubble" style="left:62px;top:480px;width:53px;height:33px">You're tired of watching others succeed while you feel stuck on the sidelines</div>
  <div class="bubble" style="left:183px;top:481px;width:57px;height:34px">You want more money, but fear of failure (and bills) keeps holding you back</div>
  <div class="bubble" style="left:125px;top:504px;width:46px;height:33px">You're done working long hours to make someone else rich</div>

  <div class="photo" style="left:262px;top:350px;width:103px;height:188px;background:linear-gradient(170deg,#c9bfb5,#6d6560 45%,#1f1d1e)" role="img" aria-label="Coach in a dark coat standing beside a luxury car"></div>
  <div class="abs note">
    <h3>You’re <span class="hl">Not Alone</span>. I’ve Been There Too.</h3>
    <p>I know how it feels to be stuck in the 9 - to - 5 grind, wishing for more but not knowing how to get started. I remember my days working long hours in a cubicle making someone rich. But I learned that success isn't about pacing yourself over decades hoping to get rich; it's about locking in for a sprint, 90 days of laser focus can completely change your life.</p>
    <p>That's how I did it. That's why I created this 90 Day step by step program to help people like YOU launch a brand confidently, even if you're starting from scratch.</p>
  </div>

  <span class="tag" style="left:234px;top:580px">OUR MISSION</span>
  <h2 class="abs center-head mis-title serif">By The End of <span class="hl">This Program</span>, You’ll:</h2>
  <div class="gain" style="left:42px;top:622px">Have a fully launched business that generates real income</div>
  <div class="gain" style="left:114px;top:622px">Gain the tools and knowledge to continue growing your business long after the sprint is over</div>
  <div class="gain" style="left:42px;top:659px">Have secured your first paying customers AND know exactly how to find more</div>
  <div class="gain" style="left:114px;top:659px">No fluff. No gimmicks. Just real results.</div>
  <div class="abs frame"><div class="photo" role="img" aria-label="The two coaches in dark suits"></div></div>
  <div class="gain" style="left:320px;top:622px">Feel confident and clear about your business strategy and next steps</div>
  <div class="gain" style="left:392px;top:622px">Go from struggling with ideas to running a profitable business in just 3 months</div>
  <div class="gain" style="left:320px;top:659px">Be one step closer to financial freedom and building generational wealth</div>
  <div class="gain" style="left:392px;top:659px">Save countless hours by following a proven roadmap instead of trial and error</div>

  <section class="abs quote">
    <div class="q-photo" role="img" aria-label="Portrait of a smiling client in a red blazer"></div>
    <span class="arrow" style="left:18px">‹</span>
    <span class="arrow" style="right:18px">›</span>
    <div class="dots"><i></i><i></i><i></i><i></i></div>
    <div class="q-body">
      <span class="tag" style="position:static">REAL PEOPLE, REAL WINS</span>
      <h3>See What’s Possible When You <span class="hl">Take Action</span></h3>
      <p>Thanks to RC's daily mentoring and assignments, I am making moves, making money and miracles around the globe! I won my first contract for $150,000. I am beyond ecstatic!</p>
      <p>I immediately found what I needed in RC's Program. It was a fully customized program that encompasses the entire aspects of success, including education, inspiration and engaging business challenges with tools that enabled me to shift my paradigm, grow my business and begin to BUILD WEALTH. The program is a game changer; no one who embraces its principles and takes massive action, remains the same.</p>
      <p class="by">~RENÉE</p>
    </div>
  </section>

  <div class="abs cta-card"></div>
  <div class="abs cta-person" role="img" aria-label="Coach in black outfit waving"></div>
  <p class="abs cta-text serif">Enrollment closes soon. Secure your spot now and start building your future! <span class="go">Join Now for 50% OFF</span></p>
  <div class="abs cta-banner"><span>THE QUARTER-YEAR<br>TYCOON</span><span class="mid" role="img" aria-label="Coaches"></span><span>LAUNCH A MILLION DOLLAR<br>BRAND IN 90 DAYS</span></div>
  <div class="abs btn">Add to Cart</div>

  <span class="tag" style="left:75px;top:1073px">TIPS</span>
  <h2 class="abs tips-title serif">There are <span class="hl">3 Killers</span> Of A<br>Great Business:</h2>
  <div class="abs tips-note"><p>Find out why businesses fail and master the strategies to overcome challenges and succeed faster than ever!</p></div>
  <article class="killer" style="left:75px">
    <div class="photo" style="background:linear-gradient(170deg,#dfe3e8,#8b847e 60%,#4a3f3a)" role="img" aria-label="Person pressing hands to face in worry"></div>
    <div class="txt"><b>Bad Habit #1</b><h4>Overthinking the First Step</h4><p>You keep planning, researching, and perfecting every little detail. But the longer you overthink, the longer you delay taking real action. Success comes from launching and refining as you go not from waiting for perfection</p></div>
  </article>
  <article class="killer" style="left:196px">
    <div class="photo" style="background:linear-gradient(170deg,#f2f2f0,#bdbdb8 60%,#5c5a57)" role="img" aria-label="Person facing a board of sketched diagrams"></div>
    <div class="txt" style="top:70px"><b>Bad Habit #2</b><h4>Waiting for the “Perfect” Time.</h4><p>You tell yourself you'll start when you have more time, money, or confidence. The truth? The "perfect" moment doesn't exist. Waiting just means missed opportunities and stagnant ideas.</p></div>
  </article>
  <article class="killer" style="left:316px">
    <div class="photo" style="background:linear-gradient(170deg,#9aa8b7,#d27a3e 60%,#5a6470)" role="img" aria-label="Laptop screen with advertising icons"></div>
    <div class="txt" style="top:70px"><b>Bad Habit #3</b><h4>Avoiding Sales and Marketing.</h4><p>You love your business idea but dread promoting it. Fear of rejection or discomfort with selling keeps you from putting your offer out there. No sales, no business - plain and simple.</p></div>
  </article>

  <span class="tag" style="left:227px;top:1315px">MEET YOUR COACHES</span>
  <h2 class="abs center-head coach-head serif">Their knowledge will make your <span class="hl">business grow rapidly</span></h2>
  <div class="abs tabs"><span class="on">Meet Dana Brooks</span><span>Meet Reggie “RC” Cole</span></div>

  <div class="fact" style="left:63px;top:1380px;width:108px"><i></i><b>#1 Bestselling Author</b> of seven books, which have sold over 3 million copies across 21 countries, with over 30 years of expertise in health, wellness, and technology.</div>
  <div class="fact" style="left:191px;top:1380px;width:108px"><i></i><b>Personal Brand Leader</b> with 2.7+ million followers across social media platforms, demonstrating strong influence and engagement.</div>
  <div class="fact" style="left:319px;top:1380px;width:121px"><i></i><b>Co-Founder of a Thriving Health Supplement Business</b>, generating $45 million in revenue within five years and serving over 400,000 customers globally.</div>
  <div class="fact" style="left:63px;top:1436px;width:108px"><i></i><b>Featured Nutrition Expert</b> on leading TV programs, talk shows and national networks across the country for many years.</div>
  <div class="fact" style="left:191px;top:1436px;width:108px"><i></i><b>Published Thought Leader</b> in premier magazines covering health, beauty, home and lifestyle.</div>
  <div class="fact" style="left:319px;top:1436px;width:121px"><i></i><b>Proven Business Strategist</b>, leveraging her experience as a top-level consultant at Harlow &amp; Pike and equity partner in a successful tech services business.</div>

  <div class="abs logos" role="img" aria-label="Media feature badges"><i></i><i></i><i></i><i></i><i></i><i></i><i></i><i></i></div>

  <div class="pic" style="left:63px;top:1538px;width:117px;height:69px;background:linear-gradient(160deg,#7c7670,#2b2726)" role="img" aria-label="Coach with a guest at an event"></div>
  <div class="pic" style="left:63px;top:1611px;width:117px;height:105px;background:linear-gradient(160deg,#3d6ea8,#7a5a48 55%,#c7a58c)" role="img" aria-label="Coach taking a selfie with a TV host"></div>
  <div class="pic" style="left:184px;top:1538px;width:135px;height:178px;background:linear-gradient(170deg,#1a1a1c,#c43636 55%,#e8e4df)" role="img" aria-label="Coaches posing with guests in red and white"></div>
  <div class="pic" style="left:324px;top:1538px;width:116px;height:105px;background:linear-gradient(160deg,#1f8fd0,#7a4e40 55%,#2b6b45)" role="img" aria-label="Coach on a TV set with a host"></div>
  <div class="pic" style="left:324px;top:1647px;width:116px;height:69px;background:linear-gradient(160deg,#5d7fa8,#2f2b31 60%,#b8b0a8)" role="img" aria-label="Coach on a talk show stage"></div>

  <section class="abs quote dark">
    <div class="q-photo" role="img" aria-label="Portrait of a smiling client in a suit"></div>
    <span class="arrow" style="left:18px">‹</span>
    <span class="arrow" style="right:18px">›</span>
    <div class="dots"><i></i><i></i><i></i></div>
    <div class="q-body">
      <span class="tag" style="position:static">BE INSPIRED</span>
      <h3>How People Just Like You Built <span class="hl">Wealth and Freedom</span></h3>
      <p>I run a seven-figure accounting company with over 25 staff members, but I'm the person who had to be on the phone with all the clients. So Reggie was immediately able to give me advice on what I needed to do to phase myself out of my own business and create processes and procedures so I can have my time back.</p>
      <p>Fast forward now, <b style="color:#fff">it's eight months later, and I've made more money than I've ever made inside of my business.</b> I now have more time to spend with my wife and doing the things that I love to do!</p>
      <p class="by">~MARCUS</p>
    </div>
  </section>

</main>
</div>
</body>
</html>
```